Short-Term Rental Website - Management Services for Property Owner

We are looking for a website to advertise our short-term rental business, Bright Door Stay Management, currently www.brightdoor.ca. Hosted on WordPress.

We have the website main page language but we are looking for someone who is creative and can present the information in a trendy, cool and professional way. I like the closed design crowd job "Plumfield Marketing - SEM, Influencer website. FUN RETRO VIBES" (see attached pictures) in terms of how the page flows, icons and stock images, other connective imagery and design features

Our main competitor website is www.stayvora.com and we like how that website feels but we like the elegance of www.Halvorn-Trask.com (desktop) and main page of www.pombridge.ca (desktop version). We like the slow type video on pombridge.com.

MUST LOOK GOOD ON MOBILE. The mobile experience has to be good.

The content in terms of the language is in one of the attached files.

Our landing page requires the following sections;
- Revenue Maximization
- Services (I have included the content that we want highlighted but we are looking for someone to be creative with how these are displayed
- Pricing
- Featured Properties (display on a carousel) *must design a carousel that can be easily populated.
- Reviews (display on a carousel) *must design a carousel that can be easily populated.
- Contact Us (first name, last name, email, phone (required), description of property)

The header will have;
- Logo (link to main page)
- Pricing (link to pricing section found on the main page)
- Services (link to services section found on the main page)
- Properties (separate page)
- Contact (link to contact area on main page)

We would also need a coded template page that we could use to add additional pages as needed.

For the properties page, we need a landing page that would allow our guests to see all of our properties and a map view with the properties plotted on the map.

As we would collect personal information we would need a cookies/ privacy policy.

The colour palette should be on the light side. We do not want the website to have a dark feel. Colours should be consistent with that of our logo but we are open to creativity.

Target Market(s)

Investment property owners

Industry/Entity Type

Real Estate

Coding

Coded - Design and coding required

Number of Pages Required

2 page

Font styles to use
Sans Serif

Requirements
Must have
• Very strong and well designed landing page

Second page which showcases properttes

Template property page that can be easily reproduced

```html
<!DOCTYPE html>
<html lang="en">
<head>
<meta charset="utf-8">
<title>Bright Door Stay Management – Pricing &amp; Featured Properties</title>
<link rel="stylesheet" href="https://fonts.googleapis.com/css2?family=Figtree:wght@400;500;600;700;800&display=swap">
<style>
  :root {
    --page: #ffffff;
    --panel: #f3f3f3;
    --teal: #4e7b87;
    --mint: #6ef0a0;
    --ink: #3d3d3d;
    --ink-soft: #2f2f2f;
    --muted: #777777;
    --line-blue: #1f5aa8;
    --card: #ffffff;
    --card-edge: #e2e2e2;
    --star: #4e7b87;
  }
  * { box-sizing: border-box; margin: 0; padding: 0; }
  html, body {
    width: 1200px; height: 1200px; overflow: hidden;
    background: var(--page);
    font-family: "Figtree", Arial, sans-serif;
    color: var(--ink);
  }
  .canvas { position: relative; width: 1200px; height: 1200px; }

  /* Pricing section */
  .pricing {
    position: absolute; left: 101px; top: 108px; width: 1005px; height: 535px;
    background: var(--panel);
  }
  .section-title {
    position: absolute; left: 0; width: 100%; text-align: center;
    font-weight: 800; color: var(--ink); letter-spacing: 0.5px;
  }
  .pricing .section-title { top: 46px; font-size: 36px; }
  .title-rule { position: absolute; height: 3px; }
  .pricing .title-rule { left: 491px; top: 90px; width: 37px; background: var(--mint); }

  .share-card {
    position: absolute; left: 90px; top: 123px; width: 331px; height: 346px;
    background: var(--teal); border-radius: 3px; color: #ffffff;
    padding: 50px 34px 0 35px;
  }
  .share-card h3 { font-size: 17.5px; font-weight: 600; line-height: 22px; letter-spacing: 0.2px; }
  .share-card .rate {
    margin-top: 24px; font-size: 72px; font-weight: 700; line-height: 64px;
    color: var(--mint); letter-spacing: -1px;
  }
  .share-card p { font-size: 11.5px; line-height: 14.5px; margin-top: 14px; }
  .share-card .rate + p { margin-top: 23px; }

  .detail-card {
    position: absolute; left: 400px; top: 176px; width: 467px; height: 262px;
    background: var(--card); border-radius: 4px;
    box-shadow: 0 2px 6px rgba(0,0,0,0.18);
    padding: 38px 44px 0 45px;
  }
  .detail-card h3 { font-size: 17px; font-weight: 400; line-height: 22px; color: var(--ink-soft); }
  .detail-card p { font-size: 11.2px; line-height: 14.5px; margin-top: 8px; color: var(--ink-soft); }
  .detail-card p + p { margin-top: 14px; }
  .example-button {
    position: absolute; left: 126px; top: 177px; width: 214px; height: 46px;
    border-radius: 14px; background: var(--teal); color: #ffffff;
    font-size: 11.5px; font-weight: 700; letter-spacing: 0.8px;
    display: flex; align-items: center; justify-content: center;
    box-shadow: 0 3px 5px rgba(0,0,0,0.22);
  }

  /* Featured properties */
  .featured { position: absolute; left: 0; top: 690px; width: 1200px; height: 510px; }
  .featured .section-title { top: 20px; font-size: 36px; }
  .featured .title-rule { left: 585px; top: 62px; width: 37px; background: var(--line-blue); height: 2px; }

  .carousel-nav { position: absolute; left: 924px; top: 98px; display: flex; align-items: center; }
  .carousel-count { font-size: 11px; color: var(--muted); margin-right: 16px; }
  .carousel-nav svg { display: block; margin-right: 4px; }

  .property-card {
    position: absolute; top: 135px; height: 281px;
    background: var(--card); border: 1px solid var(--card-edge); border-bottom: none;
    border-radius: 14px 14px 0 0; overflow: hidden;
    box-shadow: 0 1px 3px rgba(0,0,0,0.12);
    -webkit-mask-image: linear-gradient(to bottom, #000 88%, transparent 100%);
            mask-image: linear-gradient(to bottom, #000 88%, transparent 100%);
  }
  .property-card.one { left: 191px; width: 260px; }
  .property-card.two { left: 473px; width: 263px; }
  .property-card.three { left: 755px; width: 263px; }
  .property-photo { height: 175px; width: 100%; }
  .photo-living { background: linear-gradient(170deg, #d9dee4 0%, #b9c0c8 45%, #6f6a64 80%, #c9b26a 100%); }
  .photo-suite { background: linear-gradient(160deg, #9a8f84 0%, #6b625b 40%, #c3924f 75%, #3d4550 100%); }
  .photo-rooftop { background: linear-gradient(180deg, #b7bcc4 0%, #8c9aa3 35%, #6f8a63 55%, #8a8078 80%, #a9a39c 100%); }
  .property-body { padding: 14px 22px 0 23px; }
  .property-name { font-size: 11.5px; line-height: 14.5px; color: var(--ink-soft); height: 30px; }
  .property-price { margin-top: 6px; font-size: 15px; color: var(--ink-soft); }
  .property-price span { font-size: 11.5px; color: var(--muted); }
  .property-rating { margin-top: 4px; display: flex; align-items: center; font-size: 11.5px; color: var(--muted); }
  .property-rating svg { margin-right: 8px; }
</style>
</head>
<body>
<main class="canvas">

  <section class="pricing" id="pricing">
    <h2 class="section-title">PRICING</h2>
    <div class="title-rule"></div>

    <div class="share-card">
      <h3>BRIGHT DOOR'S SHARE OF THE NIGHTLY REVENUE</h3>
      <div class="rate">20%</div>
      <p>All money goes to your bank account, we invoice you one-time per month.</p>
      <p>There are no additional fees and best of all, no surprises!</p>
    </div>

    <div class="detail-card">
      <h3>Our pricing structure is simple and easy to understand, that is by design!</h3>
      <p>The nightly revenue is split between the Owner and Bright Door, 80% &amp; 20% respectively.</p>
      <p>The cleaning fee is paid for by the guest which covers all cleaning between guests. We do not take a fee from cleaning.</p>
      <div class="example-button">SEE AN EXAMPLE</div>
    </div>
  </section>

  <section class="featured" id="properties">
    <h2 class="section-title">FEATURED PROPERTIES</h2>
    <div class="title-rule"></div>

    <div class="carousel-nav">
      <span class="carousel-count">3/18</span>
      <svg width="23" height="23" viewBox="0 0 23 23" aria-label="Previous">
        <circle cx="11.5" cy="11.5" r="10.5" fill="none" stroke="#555" stroke-width="1.2"/>
        <path d="M13.5 6.5 L8.5 11.5 L13.5 16.5" fill="none" stroke="#444" stroke-width="2"/>
      </svg>
      <svg width="23" height="23" viewBox="0 0 23 23" aria-label="Next">
        <circle cx="11.5" cy="11.5" r="10.5" fill="none" stroke="#555" stroke-width="1.2"/>
        <path d="M9.5 6.5 L14.5 11.5 L9.5 16.5" fill="none" stroke="#444" stroke-width="2"/>
      </svg>
    </div>

    <article class="property-card one">
      <div class="property-photo photo-living" role="img" aria-label="Photo of a bright high-rise living room with leather sofa, yellow armchair and city view windows"></div>
      <div class="property-body">
        <div class="property-name">Parking, A+ AMENITIES &amp; view! Walk to the game!</div>
        <div class="property-price">$146 <span>/night</span></div>
        <div class="property-rating">
          <svg width="46" height="8" viewBox="0 0 46 8"><g fill="var(--star)">
            <path id="star" d="M4 0 L5 2.8 L8 2.9 L5.6 4.8 L6.5 7.8 L4 6 L1.5 7.8 L2.4 4.8 L0 2.9 L3 2.8 Z"/>
            <use href="#star" x="9.4"/><use href="#star" x="18.8"/><use href="#star" x="28.2"/><use href="#star" x="37.6"/>
          </g></svg>
          36 reviews
        </div>
      </div>
    </article>

    <article class="property-card two">
      <div class="property-photo photo-suite" role="img" aria-label="Photo of a suite living area with fireplace, wood floor, white coffee table and dark sectional sofa"></div>
      <div class="property-body">
        <div class="property-name">Snazzy Suite on Trendy West-End by Prince’s Island.</div>
        <div class="property-price">$146 <span>/night</span></div>
        <div class="property-rating">
          <svg width="46" height="8" viewBox="0 0 46 8"><g fill="var(--star)">
            <use href="#star" x="0"/><use href="#star" x="9.4"/><use href="#star" x="18.8"/><use href="#star" x="28.2"/><use href="#star" x="37.6"/>
          </g></svg>
          9 reviews
        </div>
      </div>
    </article>

    <article class="property-card three">
      <div class="property-photo photo-rooftop" role="img" aria-label="Photo of a private rooftop lounge with long bench seating, cushions and city towers"></div>
      <div class="property-body">
        <div class="property-name">Private Rooftop in Beautiful Eau Claire + Parking</div>
        <div class="property-price">$224 <span>/night</span></div>
        <div class="property-rating">
          <svg width="46" height="8" viewBox="0 0 46 8"><g fill="var(--star)">
            <use href="#star" x="0"/><use href="#star" x="9.4"/><use href="#star" x="18.8"/><use href="#star" x="28.2"/><use href="#star" x="37.6"/>
          </g></svg>
          356 reviews
        </div>
      </div>
    </article>
  </section>

</main>
</body>
</html>
```